Marlow Crest Holdings (Remodeling company) needs a logo and business card

We need a business card design for a new company. We "flip" upmarket houses (buy, remodel and sell) in the Austin, TX area. I'd like neutral colors (grey, white, gold black). I would like it to include a simple, clean logo. Our designs are modern and uncluttered and I would like that reflected in the business card design.

Target Market(s)

Young professionals, Families, Retirees. Our properties will sell for $750k+

Industry/Entity Type

Real Estate

Contact Information for Business Card

Marlow Crest Holdings
Nora Pellham
(555) 216 7042
Owner
Rory Tansil
(555) 638 1975
Realtor

Logo Text

Marlow Crest Holdings

Font styles to use
Serif
Script

Requirements
Must have
• Simple, classic design
Nice to have
• Clean lines, modern look
Should not have
• Too traditionally

```html
<!DOCTYPE html>
<html lang="en">
<head>
<meta charset="utf-8">
<title>Marlow Crest Holdings – Business Card</title>
<link rel="stylesheet" href="https://fonts.googleapis.com/css2?family=Cinzel:wght@500&family=Cormorant+Garamond:wght@500&family=Pinyon+Script&display=swap">
<style>
  :root {
    --page-bg: #e9e6e1;
    --card-charcoal: #3a3a3b;
    --card-charcoal-dark: #2c2c2d;
    --ink-white: #f4f4f2;
    --rule-grey: #bdbdbd;
    --photo-light: #ecebe6;
    --photo-mid: #cfcac1;
    --photo-wood: #6b4a33;
  }
  * { box-sizing: border-box; margin: 0; padding: 0; }
  html, body {
    width: 1200px;
    height: 780px;
    overflow: hidden;
    background: var(--page-bg);
  }
  .canvas {
    position: relative;
    width: 1200px;
    height: 780px;
    display: flex;
    align-items: center;
    justify-content: center;
  }
  .business-card {
    position: relative;
    width: 1000px;
    height: 580px;
    background: linear-gradient(160deg, var(--card-charcoal) 0%, var(--card-charcoal-dark) 100%);
    border-radius: 6px;
    overflow: hidden;
    box-shadow: 0 18px 40px rgba(0,0,0,0.25);
  }
  .card-photo-band {
    position: absolute;
    inset: 0;
    width: 100%;
    height: 100%;
  }
  .card-details {
    position: absolute;
    left: 480px;
    top: 70px;
    width: 470px;
    color: var(--ink-white);
    text-align: center;
  }
  .brand-mark {
    display: flex;
    flex-direction: column;
    align-items: center;
    gap: 18px;
  }
  .brand-rule {
    width: 340px;
    height: 1px;
    background: var(--rule-grey);
  }
  .brand-name {
    display: flex;
    align-items: center;
    gap: 14px;
    font-family: "Cinzel", serif;
    font-weight: 500;
    font-size: 34px;
    letter-spacing: 2px;
    line-height: 1.15;
    color: var(--ink-white);
  }
  .brand-square {
    width: 16px;
    height: 16px;
    background: var(--ink-white);
    flex: none;
  }
  .contact-block {
    margin-top: 58px;
  }
  .contact-name {
    font-family: "Pinyon Script", cursive;
    font-size: 66px;
    line-height: 1;
    color: var(--ink-white);
  }
  .contact-role {
    margin-top: 6px;
    font-family: "Cormorant Garamond", serif;
    font-weight: 500;
    font-size: 30px;
    letter-spacing: 1px;
  }
  .contact-phone {
    margin-top: 38px;
    font-family: "Cormorant Garamond", serif;
    font-weight: 500;
    font-size: 36px;
    letter-spacing: 1.5px;
  }
</style>
</head>
<body>
<main class="canvas">
  <article class="business-card">
    <svg class="card-photo-band" viewBox="0 0 1000 580" aria-hidden="false">
      <defs>
        <linearGradient id="interiorTones" x1="0" y1="0" x2="1" y2="1">
          <stop offset="0" stop-color="var(--photo-light)"/>
          <stop offset="0.6" stop-color="var(--photo-mid)"/>
          <stop offset="1" stop-color="var(--photo-wood)"/>
        </linearGradient>
      </defs>
      <path d="M0 0 H300 C 300 200, 470 300, 440 580 H0 Z"
            fill="url(#interiorTones)"
            role="img"
            aria-label="Photo of a bright remodeled living room with ceiling fan and wood floor"/>
      <path d="M300 0 C 300 200, 470 300, 440 580"
            fill="none" stroke="#ffffff" stroke-width="12"/>
    </svg>

    <section class="card-details">
      <div class="brand-mark">
        <span class="brand-rule"></span>
        <h1 class="brand-name"><span class="brand-square"></span>Marlow Crest Holdings</h1>
        <span class="brand-rule"></span>
      </div>

      <div class="contact-block">
        <p class="contact-name">Nora Pellham</p>
        <p class="contact-role">Owner</p>
        <p class="contact-phone">(555) 216 7042</p>
      </div>
    </section>
  </article>
</main>
</body>
</html>
```